KT Prime Motion personal training needs a new Business Card design for 2016

Business Card design:
Our current business card is very plain
We are bringing on our first team member next year and thought its a perfect time to have a new face lift for our company!

We are a Personal Training business "KT Prime Motion" who specializes in strength and conditioning / weightloss training,
We also run a yearly Bootcamp called "Ferocity Drillcamps", this is our Logo Design which we are looking for

The pink and blue in the logo are our business colours, how ever we don't want those colours to heavily dominate the card.

We are looking for a business card which is eye catching, and creative.

I am open to suggestions and any designs :)

Logo Design:

For our Logo Design we are looking for a bright, energetic logo, preferably a word logo which portrays strength and high intensity
If it has icon's etc in it thats fine again im open for suggestions :)
The Logo Design is for our Bootcamp which runs yearly
The bootcamp is called "Ferocity Drillcamp"

Target Market(s)

Age 20-40
Individuals who want to look great and have more energy

Industry/Entity Type

Business

Contact Information for Business Card

On the front
KT Prime Motion Doriel Maxton Personal Training / Bootcamps / Pilates / Nutrition Healthy mind, Healthy body, Ultimate lifestyle < our slogan
Icons for the following
Email:
Mobile:
Facebook:
Instagram:

On the back we would like to include somewhere
"Show this card to receive 50% off your first 30min pt session"
"Valid to one user only"

Logo Text

Ferocity Drillcamp

Font styles to use
Serif

Colors
e34197
0255a3
000000
ffffff

Requirements
Must have
• - Icons for instagram, facebook, email and mobile phone
• - Slogan: Healthy mind, Healthy body, Ultimate lifestyle
• - What we offer: Personal Training , Bootcamps, Pilates, Nutrition
• - Logo
• -
Nice to have
• - Our 50% offer on the back
• - a place for a photo
Should not have
• - Pink and Blue everywhere

```html
<!DOCTYPE html>
<html lang="en">
<head>
<meta charset="utf-8">
<title>KT Prime Motion – Business Card</title>
<link href="https://fonts.googleapis.com/css2?family=Saira:wght@600;700&family=Open+Sans:wght@600;700&display=swap" rel="stylesheet">
<style>
  :root {
    --blue: #1f63b0;
    --blue-light: #4f96d6;
    --pink: #e46aa8;
    --ink: #1c1d22;
    --ink-soft: #3a3c44;
    --paper: #f8fafc;
    --backdrop: #e9eaec;
    --ink-faint-blue: #b3bde0;
    --white: #ffffff;
  }
  * { margin: 0; padding: 0; box-sizing: border-box; }
  html, body { width: 1200px; height: 1000px; overflow: hidden; }
  body { background: var(--backdrop); position: relative; font-family: "Open Sans", sans-serif; }

  .card { position: absolute; left: 334px; width: 561px; height: 337px; background: var(--paper); box-shadow: 0 6px 14px rgba(0,0,0,.18); }
  .card--front { top: 141px; }
  .card--back { top: 528px; }
  .card__shapes { position: absolute; inset: 0; overflow: visible; }

  /* Front */
  .front__title { position: absolute; left: 143px; top: 8px; width: 276px; text-align: center; color: var(--white); font-family: "Saira", sans-serif; font-weight: 700; line-height: 1; }
  .front__title-main { display: block; font-size: 31px; letter-spacing: .5px; }
  .front__title-sub { display: block; font-size: 15px; letter-spacing: 3px; }

  .brand-mark { position: absolute; display: flex; align-items: center; gap: 12px; font-family: "Saira", sans-serif; font-weight: 700; letter-spacing: 1px; white-space: nowrap; }
  .brand-mark__dot { border-radius: 50%; flex: none; }
  .brand-mark--front { left: 0; right: 0; top: 104px; justify-content: center; color: var(--ink); font-size: 26px; }
  .brand-mark--front .brand-mark__dot { width: 70px; height: 70px; background: var(--blue); }
  .brand-mark--back { left: 40px; top: 190px; color: var(--ink-faint-blue); font-size: 16px; }
  .brand-mark--back .brand-mark__dot { width: 52px; height: 52px; background: var(--ink-faint-blue); }

  .front__services { position: absolute; left: 0; right: 0; top: 236px; text-align: center; color: var(--blue); font-family: "Saira", sans-serif; font-weight: 600; font-size: 12.5px; letter-spacing: 1px; }
  .front__slogan { position: absolute; left: 0; right: 0; top: 262px; text-align: center; color: var(--ink-soft); font-family: "Saira", sans-serif; font-weight: 600; font-size: 11.5px; letter-spacing: 1.5px; }
  .front__web { position: absolute; left: 106px; width: 350px; top: 310px; text-align: center; color: #dfe8f5; font-size: 11px; letter-spacing: 3.2px; font-weight: 600; }

  /* Back */
  .back__offer { position: absolute; left: 274px; top: 0; width: 287px; height: 57px; display: flex; align-items: center; justify-content: center; text-align: center; padding: 0 18px; color: var(--white); font-size: 10.5px; font-weight: 700; letter-spacing: .4px; line-height: 1.45; }
  .back__name { position: absolute; left: -14px; top: 72px; width: 281px; text-align: right; color: var(--white); font-family: "Saira", sans-serif; font-weight: 700; line-height: 1; }
  .back__name-main { display: block; font-size: 22px; letter-spacing: 1px; }
  .back__name-role { display: block; font-size: 14px; letter-spacing: 1px; margin-top: 2px; }

  .contact-list { position: absolute; left: 314px; top: 74px; list-style: none; }
  .contact-list__item { display: flex; align-items: center; height: 20px; color: var(--ink); font-weight: 700; font-size: 12px; }
  .contact-list__item + .contact-list__item { margin-top: 16px; }
  .contact-list__icon { width: 18px; height: 18px; margin-right: 16px; fill: var(--blue); flex: none; }
  .contact-list__plain { width: 16px; height: 16px; margin: 0 17px 0 1px; background: var(--blue); flex: none; }
  .contact-list__plain--round { border-radius: 50%; }

  .back__validity { position: absolute; left: 274px; top: 308px; width: 287px; height: 29px; line-height: 29px; text-align: center; color: var(--white); font-size: 11px; font-weight: 600; letter-spacing: .6px; }
</style>
</head>
<body>

<section class="card card--front" aria-label="Business card front">
  <svg class="card__shapes" width="561" height="337" viewBox="0 0 561 337">
    <rect class="band-top" x="0" y="0" width="561" height="40" fill="var(--ink)"/>
    <polygon points="119,40 143,40 143,62" fill="var(--ink-soft)"/>
    <polygon points="419,40 444,40 419,62" fill="var(--ink-soft)"/>
    <rect class="title-plate" x="143" y="0" width="276" height="62" fill="var(--pink)"/>
    <rect class="band-bottom" x="0" y="312" width="561" height="25" fill="var(--pink)"/>
    <polygon class="web-plate" points="120,299 428,299 456,337 106,337" fill="var(--blue)"/>
  </svg>
  <h1 class="front__title">
    <span class="front__title-main">KT PRIME</span>
    <span class="front__title-sub">MOTION</span>
  </h1>
  <div class="brand-mark brand-mark--front"><span class="brand-mark__dot"></span><span>KT PRIME MOTION</span></div>
  <p class="front__services">PERSONAL TRAINING / BOOTCAMPS / PILATES / NUTRITION</p>
  <p class="front__slogan">HEALTHY MIND, HEALTHY BODY, ULTIMATE LIFESTYLE</p>
  <p class="front__web">WWW.YOURWEBSITE.COM</p>
</section>

<section class="card card--back" aria-label="Business card back">
  <svg class="card__shapes" width="561" height="337" viewBox="0 0 561 337">
    <rect class="offer-block" x="274" y="0" width="287" height="57" fill="var(--ink)"/>
    <rect class="name-banner" x="-19" y="66" width="305" height="66" fill="var(--blue)"/>
    <polygon points="271,132 286,132 286,144" fill="var(--blue)"/>
    <rect class="validity-bar" x="274" y="308" width="287" height="29" fill="var(--pink)"/>
  </svg>
  <p class="back__offer">SHOW THIS CARD TO RECEIVE 50% OFF YOUR FIRST 30MIN PT SESSION</p>
  <h2 class="back__name">
    <span class="back__name-main">DORIEL MAXTON</span>
    <span class="back__name-role">TRAINER</span>
  </h2>
  <div class="brand-mark brand-mark--back"><span class="brand-mark__dot"></span><span>KT PRIME MOTION</span></div>

  <ul class="contact-list">
    <li class="contact-list__item">
      <svg class="contact-list__icon" viewBox="0 0 24 24"><path d="M6.6 10.8a15.1 15.1 0 0 0 6.6 6.6l2.2-2.2c.3-.3.7-.4 1-.2 1.1.4 2.3.6 3.6.6.6 0 1 .4 1 1V20c0 .6-.4 1-1 1A17 17 0 0 1 3 4c0-.6.4-1 1-1h3.5c.6 0 1 .4 1 1 0 1.3.2 2.5.6 3.6.1.3 0 .7-.2 1z"/></svg>
      +18 2400 5163 0418
    </li>
    <li class="contact-list__item">
      <svg class="contact-list__icon" viewBox="0 0 24 24"><path d="M12 2a10 10 0 1 0 0 20 10 10 0 0 0 0-20zm-1 17.9A8 8 0 0 1 4.1 10L9 15v1c0 1.1.9 2 2 2zm6.9-2.5c-.3-.8-1-1.4-1.9-1.4h-1v-3c0-.6-.4-1-1-1H8v-2h2c.6 0 1-.4 1-1V7h2c1.1 0 2-.9 2-2v-.4a8 8 0 0 1 2.9 12.8z"/></svg>
      WWW.COMPANY-NAME.COM
    </li>
    <li class="contact-list__item">
      <svg class="contact-list__icon" viewBox="0 0 24 24"><path d="M12 2a7 7 0 0 0-7 7c0 5.2 7 13 7 13s7-7.8 7-13a7 7 0 0 0-7-7zm0 9.5a2.5 2.5 0 1 1 0-5 2.5 2.5 0 0 1 0 5z"/></svg>
      YOUR CITY ADDRESS
    </li>
    <li class="contact-list__item">
      <svg class="contact-list__icon" viewBox="0 0 24 24"><path d="M3 6h18v12H3z"/><path d="M3.5 6.5l8.5 6.6 8.5-6.6" fill="none" stroke="var(--paper)" stroke-width="1.4"/></svg>
      YOUREMAIL@DOMAIN.COM
    </li>
    <li class="contact-list__item">
      <span class="contact-list__plain" aria-hidden="true"></span>
      /KTPRIMEMOTION
    </li>
    <li class="contact-list__item">
      <span class="contact-list__plain contact-list__plain--round" aria-hidden="true"></span>
      @KTPRIMEMOTION
    </li>
  </ul>

  <p class="back__validity">VALID TO ONE USER ONLY</p>
</section>

</body>
</html>
```